Brightfold Systems
Business Card
Professional
Daniel Harcourt
Serious Games Specialist
52 Millbrook Lane Arnprior, Ontario K7S 2B9 Canada
d.harcourt@brightfoldsys.net
http://www.brightfoldsys.net
Our company designs, operates, and supports "Serious Games" for training military, law enforcement, and government. We would like our business card to reflect this audience while maintaining the "cool" and "edgy" side of video games.
Feel the Brightfold.

```html
<!DOCTYPE html>
<html lang="en">
<head>
<meta charset="utf-8">
<title>Brightfold Systems Stationery</title>
<link href="https://fonts.googleapis.com/css2?family=Lato:wght@400;700;900&display=swap" rel="stylesheet">
<style>
:root{
  --backdrop:#8e8e8e;
  --paper:#ffffff;
  --ink:#1d2f5e;
  --accent:#2f6fc4;
  --rule:#c9ccd2;
  --muted:#6b6f78;
  --night:#111214;
}
*{margin:0;padding:0;box-sizing:border-box}
html,body{width:1200px;height:569px;overflow:hidden}
body{background:var(--backdrop);font-family:"Lato",sans-serif;position:relative;color:var(--ink)}
.sheet{position:absolute;background:var(--paper);box-shadow:0 2px 6px rgba(0,0,0,.35)}
.brand{position:absolute;display:flex;align-items:center;gap:5px;font-weight:900;color:var(--ink);white-space:nowrap;letter-spacing:.2px}
.brand .dot{border-radius:50%;background:var(--accent);flex:none}
.brand-rule{position:absolute;height:1px;background:var(--rule)}
.brand-rule::before{content:"";position:absolute;left:0;top:0;height:1px;width:22%;background:var(--accent)}
.small{position:absolute;font-size:5px;line-height:7px;color:var(--muted);text-align:right;white-space:nowrap}
.letterhead{left:43px;top:96px;width:312px;height:384px}
.letterhead-address{right:16px;top:5px;font-size:4.6px;line-height:6px}
.fax{left:379px;top:96px;width:312px;height:384px}
.fax-title{position:absolute;left:22px;top:62px;font-size:17px;font-weight:700;color:#222}
.fax-grid{position:absolute;left:22px;top:86px;width:268px;display:grid;grid-template-columns:1fr 1fr;column-gap:10px;row-gap:3px}
.fax-field{font-size:5px;color:var(--muted);border-bottom:1px solid var(--rule);height:10px;line-height:9px}
.fax-checks{position:absolute;left:22px;top:143px;width:268px;display:flex;justify-content:space-between;font-size:5px;color:var(--muted)}
.fax-checks span::before{content:"";display:inline-block;width:5px;height:5px;border:1px solid var(--muted);margin-right:3px;vertical-align:-1px}
.footer{position:absolute;bottom:12px;left:0;width:100%;text-align:center;font-size:4.5px;color:var(--muted)}
.env-back{left:780px;top:12px;width:384px;height:132px;overflow:hidden}
.env-back svg{position:absolute;left:0;top:0}
.env-front{left:768px;top:149px;width:389px;height:151px}
.env-long{left:768px;top:312px;width:389px;height:149px}
.card{position:absolute;width:118px;height:58px;box-shadow:0 2px 5px rgba(0,0,0,.4)}
.card-light{left:782px;top:499px;background:var(--paper)}
.card-dark{left:912px;top:499px;background:var(--night)}
.card-dark .brand{color:#e8ecf4}
.card-info{position:absolute;right:6px;top:8px;text-align:right;font-size:3.6px;line-height:5px;color:var(--muted);white-space:nowrap}
.card-info b{color:var(--ink);font-size:4.5px}
</style>
</head>
<body>

<section class="sheet letterhead">
  <div class="brand" style="left:22px;top:22px;font-size:10px"><span class="dot" style="width:9px;height:9px"></span>Brightfold Systems</div>
  <div class="brand-rule" style="left:0;top:39px;width:312px"></div>
  <div class="small letterhead-address">52 Millbrook Lane Arnprior, Ontario<br>K7S 2B9 Canada<br>Tel 613 555 0142<br>Fax 613 555 0143<br>http://www.brightfoldsys.net</div>
</section>

<section class="sheet fax">
  <div class="brand" style="left:22px;top:22px;font-size:10px"><span class="dot" style="width:9px;height:9px"></span>Brightfold Systems</div>
  <div class="brand-rule" style="left:0;top:39px;width:312px"></div>
  <div class="fax-title">FAX</div>
  <div class="fax-grid">
    <div class="fax-field">To:</div><div class="fax-field">From:</div>
    <div class="fax-field">Fax:</div><div class="fax-field">Pages:</div>
    <div class="fax-field">Phone:</div><div class="fax-field">Date:</div>
    <div class="fax-field">Re:</div><div class="fax-field">CC:</div>
  </div>
  <div class="fax-checks"><span>Urgent</span><span>For Review</span><span>Please Comment</span><span>Please Reply</span><span>Please Recycle</span></div>
  <div class="footer">52 Millbrook Lane Arnprior, Ontario K7S 2B9 Canada &nbsp; Tel 613 555 0142 &nbsp; d.harcourt@brightfoldsys.net</div>
</section>

<section class="sheet env-back">
  <svg width="384" height="132" viewBox="0 0 384 132" aria-hidden="true">
    <polygon points="0,0 384,0 384,52 192,82 0,52" fill="var(--night)"/>
    <polyline points="0,52 192,82 384,52" fill="none" stroke="#d7d9de" stroke-width="1"/>
    <polyline points="0,132 192,92 384,132" fill="none" stroke="#e2e4e8" stroke-width="1"/>
  </svg>
  <div class="brand" style="left:148px;top:22px;font-size:10px;color:#e8ecf4"><span class="dot" style="width:9px;height:9px"></span>Brightfold Systems</div>
</section>

<section class="sheet env-front">
  <div class="brand" style="left:18px;top:40px;font-size:10px"><span class="dot" style="width:9px;height:9px"></span>Brightfold Systems</div>
  <div class="brand-rule" style="left:0;top:56px;width:389px"></div>
  <div class="small" style="right:16px;top:44px">52 Millbrook Lane Arnprior, Ontario K7S 2B9 Canada</div>
  <div class="small" style="right:16px;top:130px">http://www.brightfoldsys.net</div>
</section>

<section class="sheet env-long">
  <div class="brand" style="left:18px;top:20px;font-size:10px"><span class="dot" style="width:9px;height:9px"></span>Brightfold Systems</div>
  <div class="brand-rule" style="left:0;top:36px;width:389px"></div>
  <div class="small" style="left:18px;top:46px;text-align:left">52 Millbrook Lane Arnprior, Ontario K7S 2B9 Canada</div>
  <div class="small" style="right:16px;top:128px">http://www.brightfoldsys.net</div>
</section>

<section class="card card-light">
  <div class="brand" style="left:6px;top:10px;font-size:5.5px;gap:3px"><span class="dot" style="width:5px;height:5px"></span>Brightfold Systems</div>
  <div class="card-info"><b>Daniel Harcourt</b><br>Serious Games Specialist<br><br>Tel 613 555 0142<br>d.harcourt@brightfoldsys.net<br>52 Millbrook Lane Arnprior, Ontario</div>
</section>

<section class="card card-dark">
  <div class="brand" style="left:24px;top:22px;font-size:8px;gap:4px"><span class="dot" style="width:7px;height:7px"></span>Brightfold Systems</div>
</section>

</body>
</html>
```